弊社は健診に携わる医療機関様向けに、さまざまな周辺サービスのお手伝いをさせていただいております。その中で、最も営業に力を注いでいきたいサービスが、「コールセンター」となっております。
既に「コールセンター」のチラシを持っておりますが、より詳細な業務内容をアピールしたく、この度、作品を募集いたします。
A4サイズのaiデータでの納品をお願いいたします。

この度はご提案いただき、ありがとうございました。
両面を使い、サービスの内容を細かく、且つわかりやすくまとめていただきましたので、決定いたしました。

素敵なDMのご提案、誠にありがとうございました。
また機会がございましたら、宜しくお願いいたします。

```html
<!DOCTYPE html>
<html lang="ja">
<head>
<meta charset="utf-8">
<title>健康診断コールセンターサービス</title>
<link rel="stylesheet" href="https://fonts.googleapis.com/css2?family=Noto+Sans+JP:wght@400;500;700;900&family=Noto+Serif+JP:wght@700;900&display=swap">
<style>
  :root {
    --orange: #f08c1e;
    --orange-deep: #e8731a;
    --orange-pale: #fdeee0;
    --ink: #3a3a3a;
    --muted: #5c5c5c;
    --white: #ffffff;
    --navy: #1d3a6e;
  }
  * { margin: 0; padding: 0; box-sizing: border-box; }
  html, body { width: 846px; height: 1200px; overflow: hidden; background: var(--white); }
  body { font-family: "Noto Sans JP", sans-serif; color: var(--ink); }
  .flyer { position: relative; width: 846px; height: 1200px; overflow: hidden; background: var(--white); }

  .hero-photo {
    position: absolute; left: 0; top: 0; width: 846px; height: 720px;
    background: linear-gradient(115deg, #f4f4f3 0%, #e9e7e4 45%, #d8d3cd 70%, #c9c3bc 100%);
  }

  .title-block { position: absolute; left: 34px; top: 112px; }
  .title-line {
    display: inline-block; background: var(--orange); color: var(--white);
    font-weight: 900; letter-spacing: 4px; line-height: 1; padding: 10px 16px 12px;
  }
  .title-line.main { font-size: 54px; }
  .title-line.sub { font-size: 54px; margin-top: 10px; }
  .title-row { display: flex; align-items: flex-end; gap: 12px; }
  .title-target { color: var(--orange-deep); font-size: 30px; font-weight: 700; padding-bottom: 8px; letter-spacing: 1px; }

  .record-badge {
    position: absolute; left: 430px; top: 50px; width: 150px; height: 150px; border-radius: 50%;
    background: var(--white); box-shadow: 0 2px 8px rgba(0,0,0,.15);
    display: flex; flex-direction: column; align-items: center; justify-content: center;
    font-family: "Noto Serif JP", serif; color: #222;
  }
  .record-badge .big { font-size: 40px; font-weight: 900; line-height: 1; }
  .record-badge .big small { font-size: 26px; }
  .record-badge .small { font-size: 22px; font-weight: 700; margin-top: 4px; }

  .lower { position: absolute; left: 0; top: 720px; width: 846px; height: 420px; background: var(--orange-pale); }

  .lead-banner {
    position: absolute; left: 90px; top: 688px; width: 666px; height: 60px;
    background: var(--white); border: 3px solid var(--orange);
    display: flex; align-items: center; justify-content: center; gap: 14px;
    font-size: 29px; font-weight: 900; letter-spacing: 1px;
  }
  .lead-banner .mark { width: 26px; height: 26px; background: var(--orange); }
  .lead-banner::after {
    content: ""; position: absolute; left: 50%; bottom: -16px; margin-left: -16px;
    border: 16px solid transparent; border-bottom: 0; border-top-color: var(--orange);
  }

  .intro { position: absolute; left: 0; top: 766px; width: 846px; text-align: center; font-size: 19px; font-weight: 700; line-height: 1.6; }
  .intro .hl { color: var(--orange-deep); }

  .points { position: absolute; left: 34px; top: 846px; width: 778px; display: flex; gap: 24px; }
  .point-card { flex: 1; background: var(--white); border: 2px solid var(--orange); padding: 24px 14px 12px; position: relative; height: 192px; }
  .point-tag {
    position: absolute; left: 10px; top: -12px; background: var(--orange); color: var(--white);
    font-size: 13px; font-weight: 700; letter-spacing: 1px; padding: 2px 10px;
  }
  .point-title {
    text-align: center; font-family: "Noto Serif JP", serif; font-size: 22px; font-weight: 900;
    line-height: 1.35; border-bottom: 1px dashed var(--orange); padding-bottom: 8px; white-space: nowrap;
  }
  .point-title .hl { color: var(--orange-deep); font-size: 26px; }
  .point-text { font-size: 12.5px; line-height: 1.6; color: var(--muted); margin-top: 8px; }

  .extra { position: absolute; left: 34px; top: 1054px; width: 778px; height: 76px; display: flex; align-items: center; }
  .extra-mark {
    width: 76px; height: 76px; border-radius: 50%; background: var(--orange); color: var(--white);
    display: flex; align-items: center; justify-content: center; font-size: 20px; font-weight: 900; flex-shrink: 0; z-index: 1;
  }
  .extra-box { margin-left: -20px; padding: 8px 12px 8px 34px; background: var(--white); border: 2px solid var(--orange); flex: 1; }
  .extra-head { font-size: 21px; font-weight: 900; }
  .extra-head .hl { color: var(--orange-deep); }
  .extra-text { font-size: 11.5px; color: var(--muted); line-height: 1.5; margin-top: 2px; }

  .company { position: absolute; left: 0; top: 1148px; width: 846px; display: flex; align-items: center; justify-content: center; gap: 12px; }
  .company-dot { width: 30px; height: 30px; border-radius: 50%; background: var(--navy); }
  .company-name { font-size: 25px; font-weight: 700; color: var(--navy); }
</style>
</head>
<body>
<main class="flyer">
  <div class="hero-photo" role="img" aria-label="ヘッドセットを着けたオペレーターがキーボードで入力している写真"></div>

  <div class="title-block">
    <h1 class="title-line main">健康診断</h1><br>
    <div class="title-line sub">コールセンター</div><br>
    <div class="title-row">
      <div class="title-line sub">サービス</div>
      <span class="title-target">［医療機関様向け］</span>
    </div>
  </div>

  <div class="record-badge">
    <div class="big">20<small>万件</small></div>
    <div class="small">の実績</div>
  </div>

  <section class="lower"></section>

  <h2 class="lead-banner"><span class="mark"></span>面倒な事務作業を弊社が代行致します</h2>

  <p class="intro">
    医療機関様が<span class="hl">コア業務に集中</span>していただくため、<br>
    <span class="hl">予約受付コールセンター業務</span>を<span class="hl">専門チーム</span>がお手伝いさせていただきます。
  </p>

  <div class="points">
    <article class="point-card">
      <span class="point-tag">POINT.01</span>
      <h3 class="point-title">院内スタッフの<br><span class="hl">負担を軽減</span></h3>
      <p class="point-text">予約受付業務をアウトソースすることで、他の業務に集中することが出来ます。</p>
    </article>
    <article class="point-card">
      <span class="point-tag">POINT.02</span>
      <h3 class="point-title">変動費のため<br><span class="hl">人件費削減</span>に</h3>
      <p class="point-text">受付業務に必要な人件費を変動費として抑え、コスト削減につながります。</p>
    </article>
    <article class="point-card">
      <span class="point-tag">POINT.03</span>
      <h3 class="point-title">対応は<span class="hl">経験豊富</span>な<br><span class="hl">オペレーター</span></h3>
      <p class="point-text">専門オペレーターが丁寧に対応し、受診者様に安心をお届けします。</p>
    </article>
  </div>

  <div class="extra">
    <div class="extra-mark">さらに</div>
    <div class="extra-box">
      <p class="extra-head">お客様のご希望に合わせた<span class="hl">オーダーメイド業務フロー</span>が可能です</p>
      <p class="extra-text">受付・連絡方法や、インバウンドのみ、アウトバウンドなど、ご希望に合わせた業務フローに対応します。<br>既存のマニュアルやトークスクリプトも活用し、柔軟にご提案いたします。</p>
    </div>
  </div>

  <footer class="company">
    <span class="company-dot"></span>
    <span class="company-name">株式会社メディコールサポート</span>
  </footer>
</main>
</body>
</html>
```